TRW General Contracting

Roofing, Siding,windows, doors, Gutter,additions, decks, garagesand hanyman services fully insured and licensed, free estimates, accept all major credit cards call (614)392-7705 email corvinwr@mailbrook.net

Target Market(s)

Home improvement

Industry/Entity Type

Home Improvement

Requirements
Must have
• Whats listed above
Nice to have
• I dont have a logo i want wording for roofing, siding, gutter, decks, additions, windows, doors, and handyman services with my phone # 614-392-7705 and email corvinwr@mailbrook.net

```html
<!DOCTYPE html>
<html lang="en">
<head>
<meta charset="utf-8">
<title>TRW General Contracting – Flyer</title>
<link rel="stylesheet" href="https://fonts.googleapis.com/css2?family=Jost:wght@400;500;600;700&family=Oswald:wght@600;700&display=swap">
<style>
  :root {
    --page: #e9e6e1;
    --sheet: #f1f1f1;
    --cyan: #8fdbe4;
    --cyan-light: #b8ecf1;
    --ink: #111111;
    --white: #ffffff;
    --gold: #f6c200;
    --tile-bar: #2a2a2a;
    --red: #c3161c;
    --red-dark: #8e0c10;
    --blue: #1d5f9e;
    --body: #1e1e1e;
  }
  * { box-sizing: border-box; margin: 0; padding: 0; }
  html, body {
    width: 1200px; height: 1067px; overflow: hidden;
    background: var(--page);
  }
  .flyer {
    position: absolute; left: 48px; top: 109px;
    width: 1104px; height: 849px;
    background: var(--sheet);
    overflow: hidden;
    box-shadow: 0 6px 18px rgba(0,0,0,.18);
    font-family: "Jost", "Helvetica Neue", Arial, sans-serif;
  }
  .backdrop { position: absolute; inset: 0; }

  .headline {
    position: absolute; left: 0; top: 40px; width: 472px; height: 133px;
    background: var(--ink); color: var(--white);
    font-weight: 700; font-size: 54px; line-height: 54px;
    padding: 12px 0 0 58px; letter-spacing: .5px;
  }

  .service {
    position: absolute; width: 185px; height: 130px;
    border: 4px solid var(--gold);
    box-shadow: 0 3px 6px rgba(0,0,0,.25);
    overflow: hidden;
  }
  .service-photo { position: absolute; inset: 0; }
  .service-label {
    position: absolute; left: 0; right: 0; bottom: 0;
    background: rgba(34,34,34,.92); color: var(--white);
    font-weight: 500; font-size: 21px; line-height: 21px;
    text-align: center; padding: 7px 0 6px;
  }
  .service-label.two-line { font-size: 19px; line-height: 19px; padding: 4px 0 4px; }

  .contractor-photo {
    position: absolute; left: 49px; top: 196px; width: 382px; height: 599px;
    background: linear-gradient(180deg, #6b5a4f 0%, #3f5479 35%, #3a4a66 62%, #2f3d58 100%);
    border-radius: 160px 160px 20px 20px;
    opacity: .9;
  }

  .estimate-badge {
    position: absolute; left: 446px; top: 382px; width: 416px; height: 173px;
    background: var(--red);
    border: 4px solid var(--white);
    outline: 3px solid var(--red-dark);
    color: var(--white);
    font-family: "Oswald", "Arial Narrow", sans-serif; font-weight: 700;
    text-transform: uppercase;
  }
  .estimate-badge .call { position: absolute; left: 28px; top: 12px; font-size: 42px; line-height: 40px; }
  .estimate-badge .free { position: absolute; left: 218px; top: 6px; font-size: 88px; line-height: 88px; }
  .estimate-badge .estimates { position: absolute; left: 26px; top: 90px; font-size: 68px; line-height: 68px; letter-spacing: 1px; }

  .cards-note {
    position: absolute; left: 434px; top: 582px;
    color: var(--blue); font-weight: 500; font-size: 34px; letter-spacing: .3px;
    white-space: nowrap;
  }
  .credentials {
    position: absolute; left: 434px; top: 646px;
    color: var(--body); font-weight: 400; font-size: 26px; line-height: 33px;
    text-transform: uppercase;
  }

  .brand {
    position: absolute; left: 760px; top: 690px; width: 300px;
    display: flex; align-items: center; gap: 12px;
  }
  .brand-mark { width: 26px; height: 26px; background: var(--red); flex: none; }
  .brand-name { color: var(--red); font-weight: 700; font-size: 25px; line-height: 30px; }

  .contact-bar { position: absolute; left: 0; top: 795px; width: 1104px; height: 54px; }
  .contact-email {
    position: absolute; left: 58px; top: 804px;
    font-weight: 500; font-size: 29px; color: var(--ink);
  }
  .contact-phone {
    position: absolute; right: 44px; top: 802px;
    font-weight: 700; font-size: 32px; color: var(--white); letter-spacing: .4px;
  }
</style>
</head>
<body>
<main class="flyer">
  <svg class="backdrop" width="1104" height="849" viewBox="0 0 1104 849" aria-hidden="true">
    <polygon points="0,0 370,0 722,849 0,849" fill="var(--cyan)"/>
    <polygon points="370,0 420,0 772,849 722,849" fill="var(--cyan-light)"/>
  </svg>

  <h1 class="headline">WE ARE THE<br>EXPERT IN</h1>

  <div class="service" style="left:488px; top:38px;">
    <div class="service-photo" role="img" aria-label="Photo of a house with a new roof" style="background:linear-gradient(180deg,#9cc4e6 0%,#5f8a5a 45%,#7b7f86 100%);"></div>
    <div class="service-label">ROOFING</div>
  </div>
  <div class="service" style="left:685px; top:38px;">
    <div class="service-photo" role="img" aria-label="Photo of houses with new siding" style="background:linear-gradient(90deg,#d9d2c0 0%,#b9a88a 40%,#8f6f5e 70%,#cfc6b6 100%);"></div>
    <div class="service-label">SIDING</div>
  </div>
  <div class="service" style="left:882px; top:38px;">
    <div class="service-photo" role="img" aria-label="Photo of a room with new windows and doors" style="background:linear-gradient(180deg,#e8e4d8 0%,#c9c2ad 60%,#a9987b 100%);"></div>
    <div class="service-label two-line">WINDOWS<br>&amp; DOORS</div>
  </div>
  <div class="service" style="left:685px; top:190px;">
    <div class="service-photo" role="img" aria-label="Photo of a roof edge with a gutter" style="background:linear-gradient(180deg,#f2f2f2 0%,#d6d6d6 50%,#6b6b6b 100%);"></div>
    <div class="service-label">GUTTER</div>
  </div>
  <div class="service" style="left:882px; top:190px;">
    <div class="service-photo" role="img" aria-label="Photo of a framed home addition under construction" style="background:linear-gradient(180deg,#cfb08a 0%,#a8825c 55%,#7a5b3f 100%);"></div>
    <div class="service-label">ADDITIONS</div>
  </div>
  <div class="service" style="left:882px; top:342px;">
    <div class="service-photo" role="img" aria-label="Photo of a wooden deck with railing" style="background:linear-gradient(180deg,#8fb7dd 0%,#b26a3c 45%,#e3e0da 80%,#bdb6aa 100%);"></div>
    <div class="service-label">DECKS</div>
  </div>

  <div class="contractor-photo" role="img" aria-label="Photo of a contractor in a plaid shirt and tool belt, kneeling and pointing to the offer"></div>

  <div class="estimate-badge">
    <span class="call">CALL NOW<br>FOR A</span>
    <span class="free">FREE</span>
    <span class="estimates">ESTIMATES</span>
  </div>

  <p class="cards-note">ACCEPT ALL MAJOR CREDIT CARDS</p>

  <p class="credentials">Garagesand<br>Hanyman services<br>Fully insured<br>and licensed</p>

  <div class="brand">
    <span class="brand-mark"></span>
    <span class="brand-name">TRW General Contracting</span>
  </div>

  <svg class="contact-bar" width="1104" height="54" viewBox="0 0 1104 54" aria-hidden="true">
    <polygon points="0,0 590,0 570,54 0,54" fill="var(--gold)"/>
    <polygon points="590,0 1104,0 1104,54 570,54" fill="var(--red)"/>
    <polygon points="584,0 600,0 580,54 564,54" fill="var(--ink)"/>
  </svg>
  <p class="contact-email">Mail Us-corvinwr@mailbrook.net</p>
  <p class="contact-phone">CALL US (614)392-7705</p>
</main>
</body>
</html>
```